Med Spa business card design with logo

Need a logo design and business card for our new company Verbena Aesthetics Med Spa. We are a medical office that deals with high end clients. We offer them skin care products which include DERMIQ, lip augmentation, and various laser for the skin. I king of like the logo attached, maybe something along those lines but also open to any logo concept.
Updates

Target Market(s)

Out target audience are male and females in the age range of 21-80 years of age

Industry/Entity Type

Medical

Contact Information for Business Card

woukd like front of card to have logo and business name VERBENA AESTHETICS MEDSPA. Back of card employee name and phone number along with instagram logo and user name

Font styles to use
Serif
Sans Serif

Requirements
Must have
• prefer monochromatic look white, black, gold
Should not have
• not too colorful

```html
<!DOCTYPE html>
<html lang="en">
<head>
<meta charset="utf-8">
<title>Verbena Aesthetics Med Spa – Business Card</title>
<link href="https://fonts.googleapis.com/css2?family=Bodoni+Moda:wght@500&family=Montserrat:wght@400;500&display=swap" rel="stylesheet">
<style>
  :root {
    --backdrop: #eeeeee;
    --card: #f7f7f6;
    --card-edge: #e2e2e0;
    --rose-gold: #c4917b;
    --ink: #2b2b2b;
  }
  * { box-sizing: border-box; margin: 0; padding: 0; }
  html, body {
    width: 1200px; height: 1000px; overflow: hidden;
    background: var(--backdrop);
  }
  .canvas { position: relative; width: 1200px; height: 1000px; }

  .card {
    position: absolute;
    width: 600px; height: 343px;
    background: var(--card);
    border: 1px solid var(--card-edge);
  }
  .card--front { left: 540px; top: 90px; }
  .card--back  { left: 60px;  top: 560px; }

  /* Front */
  .brand {
    position: absolute; inset: 0;
    display: flex; flex-direction: column; align-items: center; justify-content: center;
    color: var(--rose-gold);
  }
  .brand__dot {
    width: 56px; height: 56px; border-radius: 50%;
    border: 2px solid var(--rose-gold);
    margin-bottom: 22px;
  }
  .brand__name {
    font-family: "Bodoni Moda", serif; font-weight: 500;
    font-size: 26px; letter-spacing: 3px;
  }
  .brand__tag {
    font-family: "Bodoni Moda", serif; font-weight: 500;
    font-size: 10px; letter-spacing: 6px; margin-top: 6px;
  }

  /* Back */
  .person {
    position: absolute; left: 170px; top: 60px; width: 400px; text-align: center;
  }
  .person__name {
    font-family: "Bodoni Moda", serif; font-weight: 500;
    font-size: 38px; letter-spacing: 4px; color: var(--rose-gold);
  }
  .person__role {
    font-family: "Montserrat", sans-serif; font-weight: 500;
    font-size: 13px; letter-spacing: 4px; color: var(--ink); margin-top: 8px;
  }
  .contact {
    position: absolute;
    display: flex; align-items: center; gap: 14px;
    font-family: "Montserrat", sans-serif; font-size: 16px;
    letter-spacing: 6px; color: var(--ink);
  }
  .contact--email { left: 40px; top: 185px; }
  .contact--social { left: 150px; top: 235px; }
  .contact--phone { left: 340px; top: 285px; }
  .contact__icon { width: 20px; height: 20px; flex: none; }
  .contact__square { width: 16px; height: 16px; background: var(--rose-gold); flex: none; }
</style>
</head>
<body>
<main class="canvas">

  <section class="card card--front" aria-label="Card front">
    <div class="brand">
      <span class="brand__dot"></span>
      <span class="brand__name">VERBENA AESTHETICS</span>
      <span class="brand__tag">MEDSPA</span>
    </div>
  </section>

  <section class="card card--back" aria-label="Card back">
    <div class="person">
      <p class="person__name">NAME SURNAME</p>
      <p class="person__role">POSITION</p>
    </div>

    <p class="contact contact--email">
      <svg class="contact__icon" viewBox="0 0 20 20" aria-hidden="true">
        <rect x="1" y="4" width="18" height="12" fill="var(--rose-gold)"/>
        <path d="M1 4 L10 11 L19 4" fill="none" stroke="var(--card)" stroke-width="1.4"/>
      </svg>
      email@email.com
    </p>

    <p class="contact contact--social">
      <span class="contact__square"></span>
      @instagram
    </p>

    <p class="contact contact--phone">
      <svg class="contact__icon" viewBox="0 0 20 20" aria-hidden="true">
        <path d="M5 2 L8 2 L9 6 L7 8 Q8.5 11.5 12 13 L14 11 L18 12 L18 15 Q18 18 15 18 Q3 16 2 5 Q2 2 5 2 Z" fill="var(--rose-gold)"/>
      </svg>
      123456789
    </p>
  </section>

</main>
</body>
</html>
```